Fact/Marketing Sheet(s) for Health & Wellness Plan

We are wanting to market a new program that we have for Health & Wellness Benefits for our customer Northfield Federation of Rural Fairs (NFRF). We would like to present this information in a professional format that compels the recipient/reader to act on this.
I like the format of the UofK document (see attahed)- however would adjust the photo to be something Agricultural related.
I am very interested to see other ideas that may be proposed.
In addition to the content that we are wanting to communicate at this time (see attached (NFRF Project ) I have also included our Style Guide , logos, and pattern if needed.
Members of the Northfield Federation of Rural Fairs - typically business leaders and volunteers in communities across Alberta.
- In Brand Document

```html
<!DOCTYPE html>
<html lang="en">
<head>
<meta charset="utf-8">
<title>Health and Wellness Benefits Program</title>
<link href="https://fonts.googleapis.com/css2?family=Montserrat:wght@700;800&family=Jost:wght@400;500;600&family=Libre+Baskerville&display=swap" rel="stylesheet">
<style>
  :root {
    --navy: #141d5c;
    --navy-deep: #0f1850;
    --brand-blue: #2150a6;
    --heading-blue: #1f4aa3;
    --icon-blue: #23407f;
    --panel-grey: #dcdad6;
    --rule-grey: #8a8a8a;
    --ink: #3a3a3a;
    --ink-soft: #4a4a4a;
    --white: #ffffff;
  }
  * { margin: 0; padding: 0; box-sizing: border-box; }
  html, body { width: 1200px; height: 800px; overflow: hidden; background: var(--white); }
  .sheet { position: relative; width: 1200px; height: 800px; overflow: hidden; font-family: "Jost", sans-serif; color: var(--ink); }

  .masthead {
    position: absolute; left: 0; top: 0; width: 1200px; height: 171px;
    background: linear-gradient(120deg, var(--navy-deep) 0%, var(--navy) 60%, #18226a 100%);
  }
  .masthead-title {
    position: absolute; left: 52px; top: 40px;
    font-family: "Montserrat", sans-serif; font-weight: 800;
    font-size: 43px; line-height: 54px; letter-spacing: 0.5px; color: var(--white);
  }
  .org-mark {
    position: absolute; left: 843px; top: 54px; width: 296px; height: 58px;
    background: var(--white); border-radius: 6px;
    display: flex; align-items: center; gap: 12px; padding: 0 14px;
  }
  .org-dot { width: 30px; height: 30px; border-radius: 50%; background: var(--brand-blue); flex: none; }
  .org-name {
    font-family: "Jost", sans-serif; font-weight: 600; font-size: 15px; line-height: 18px;
    text-transform: uppercase; color: var(--navy);
  }

  .highlights { position: absolute; left: 0; top: 171px; width: 767px; height: 507px; background: var(--white); }
  .highlights-label {
    position: absolute; left: 52px; top: 33px;
    font-family: "Jost", sans-serif; font-weight: 400; font-size: 30px; line-height: 33px;
    color: var(--heading-blue); text-transform: uppercase;
  }
  .highlights-rule { position: absolute; left: 241px; top: 33px; width: 4px; height: 65px; background: var(--rule-grey); }
  .highlights-intro {
    position: absolute; left: 271px; top: 40px; width: 470px;
    font-size: 17px; line-height: 24px; color: var(--ink-soft);
  }
  .feature { position: absolute; width: 320px; text-align: center; }
  .feature svg { display: block; margin: 0 auto; }
  .feature-text { margin-top: 20px; font-size: 19px; line-height: 26px; color: var(--ink); }
  .feature--protection { left: 53px; top: 138px; }
  .feature--guarantee { left: 432px; top: 138px; }
  .feature--exclusive { left: 53px; top: 325px; }
  .feature--enrolment { left: 432px; top: 325px; }

  .coverages { position: absolute; left: 767px; top: 171px; width: 433px; height: 507px; background: var(--panel-grey); }
  .coverages-title {
    position: absolute; left: 39px; top: 36px;
    font-family: "Libre Baskerville", serif; font-size: 29px; color: var(--navy);
  }
  .coverage-list { position: absolute; left: 41px; top: 97px; width: 360px; list-style: none; }
  .coverage-list li { display: flex; font-size: 18px; line-height: 26px; color: var(--ink); margin-bottom: 10.5px; }
  .coverage-num { width: 27px; flex: none; }
  .coverages-note { position: absolute; left: 41px; top: 429px; font-size: 11.5px; line-height: 21px; color: var(--ink); }

  .apply-band { position: absolute; left: 0; top: 678px; width: 1200px; height: 122px; background: var(--brand-blue); color: var(--white); }
  .apply-lead { position: absolute; left: 52px; top: 24px; font-size: 23px; line-height: 30px; }
  .apply-contact { position: absolute; left: 52px; top: 63px; font-size: 24px; line-height: 32px; }
  .apply-contact strong { font-weight: 600; }
</style>
</head>
<body>
<main class="sheet">
  <header class="masthead">
    <h1 class="masthead-title">HEALTH AND WELLNESS<br>BENEFITS PROGRAM</h1>
    <div class="org-mark">
      <span class="org-dot"></span>
      <span class="org-name">Northfield Federation<br>of Rural Fairs</span>
    </div>
  </header>

  <section class="highlights">
    <h2 class="highlights-label">Program<br>Highlights</h2>
    <div class="highlights-rule"></div>
    <p class="highlights-intro">Flexible coverage options with the ability to build your own plan that is best for your employees and board members</p>

    <div class="feature feature--protection">
      <svg width="30" height="36" viewBox="0 0 30 36" aria-hidden="true">
        <path d="M15 1 L28 6 V16 C28 25 22 31 15 35 C8 31 2 25 2 16 V6 Z" fill="none" stroke="var(--icon-blue)" stroke-width="3"/>
        <path d="M15 3 V18 H4 V7 Z" fill="var(--icon-blue)"/>
        <path d="M15 18 H26 C25 25 20 30 15 33 Z" fill="var(--icon-blue)"/>
      </svg>
      <p class="feature-text">Added protection for your<br>employees/board members<br>and their families</p>
    </div>

    <div class="feature feature--guarantee">
      <svg width="34" height="40" viewBox="0 0 34 40" aria-hidden="true">
        <path d="M9 24 L4 37 L10 35 L13 40 L17 29 Z M25 24 L30 37 L24 35 L21 40 L17 29 Z" fill="var(--icon-blue)"/>
        <circle cx="17" cy="15" r="14" fill="var(--icon-blue)"/>
        <circle cx="17" cy="15" r="9" fill="none" stroke="var(--white)" stroke-width="2"/>
        <path d="M17 9.5 L18.6 13.3 L22.6 13.5 L19.5 16 L20.5 20 L17 17.8 L13.5 20 L14.5 16 L11.4 13.5 L15.4 13.3 Z" fill="var(--white)"/>
      </svg>
      <p class="feature-text">Guaranteed issue<br>with no medical<br>underwriting</p>
    </div>

    <div class="feature feature--exclusive">
      <svg width="38" height="38" viewBox="0 0 38 38" aria-hidden="true">
        <circle cx="19" cy="19" r="16.5" fill="none" stroke="var(--icon-blue)" stroke-width="3.5"/>
        <path d="M19 8 L22 15.2 L29.6 15.6 L23.7 20.4 L25.6 28 L19 23.8 L12.4 28 L14.3 20.4 L8.4 15.6 L16 15.2 Z" fill="var(--icon-blue)"/>
      </svg>
      <p class="feature-text">Exclusive to existing members of<br>the Northfield Federation<br>of Rural Fairs</p>
    </div>

    <div class="feature feature--enrolment">
      <svg width="42" height="34" viewBox="0 0 42 34" aria-hidden="true">
        <rect x="1" y="1" width="34" height="24" rx="3" fill="var(--icon-blue)"/>
        <rect x="1" y="7" width="34" height="5" fill="var(--white)"/>
        <rect x="5" y="16" width="8" height="3" fill="var(--white)"/>
        <rect x="15" y="16" width="6" height="3" fill="var(--white)"/>
        <circle cx="33" cy="25" r="8.5" fill="var(--icon-blue)" stroke="var(--white)" stroke-width="2"/>
        <path d="M29 25 L32 28 L37 22" fill="none" stroke="var(--white)" stroke-width="2.2"/>
      </svg>
      <p class="feature-text">Simple and easy<br>enrollment with convenient<br>payment options</p>
    </div>
  </section>

  <aside class="coverages">
    <h2 class="coverages-title">Coverages Available</h2>
    <ol class="coverage-list">
      <li><span class="coverage-num">1.</span><span>Health Spending Accounts / Taxable Wellness Accounts</span></li>
      <li><span class="coverage-num">2.</span><span>Life &amp; Disability Insurance</span></li>
      <li><span class="coverage-num">3.</span><span>Critical Illness</span></li>
      <li><span class="coverage-num">4.</span><span>Employee &amp; Family Assistance Program</span></li>
      <li><span class="coverage-num">5.</span><span>Medical Second Opinion</span></li>
      <li><span class="coverage-num">6.</span><span>Accidental Death and Dismemberment</span></li>
      <li><span class="coverage-num">7.</span><span>Hospital Cash</span></li>
      <li><span class="coverage-num">8.</span><span>Final Expenses</span></li>
    </ol>
    <p class="coverages-note">*Policies are subject to standard conditions and exclusions.<br>Please refer to the specific policy wordings for complete details.</p>
  </aside>

  <footer class="apply-band">
    <p class="apply-lead">To apply, please contact our broker partner, Maple Crest Brokers at</p>
    <p class="apply-contact"><strong>(780) 555-0148</strong> or <strong>benefits@maplecrest.ca</strong></p>
  </footer>
</main>
</body>
</html>
```